Business Card

I need a business card that is fresh, styling and reflects my heart centered healing business while still maintaining full professionalism as I have an my evidence-based practice. I am a Naturopath and a Shiatsu Massage Therapist.
Below are my existing logo (file 1) and an inspiration image (file 2) that reflects the colours and style I would like to express to my card (blues greens). I especially like that tree wallpaper.

Information for the card:
Tessa Gorrinde
BHSc. (Nat) m.QRPC
Naturopath
Herbalist
Nutritionist
Shiatsu Therapist
Wellness Counsellor

41 Dovertan St South Karrowby
www.tessagorrinde.com.au
tessa@tessagorrinde.com.au

NOte: I've removed part of the brief, in that I've changed my mind about the back of the card being a '5 treatments and get sixth one free" I'd rather have this on a separate card. So please do not include this in your designs.
Updates

Hi Guys, I've taken the '5 session get the sixth free' part out of the brief. Also, I've added the info to go on the business card into the brief.

Thanks and happy designing
Tes

I've just uploaded a high res better quality version of the hand logo. Thanks Lovlies. 

Target Market(s)

I am targeting western women of ages 25 - 40 in preconception care, sugar addiction therapy, and wellness coaching. I want must card to be vibrant, positive and current.

Industry/Entity Type

Business

Requirements
Must have
• Please include my hand image logo

```html
<!DOCTYPE html>
<html lang="en">
<head>
<meta charset="utf-8">
<title>Tessa Shiatsu – Business Card</title>
<link href="https://fonts.googleapis.com/css2?family=Josefin+Sans:wght@300;400;600&display=swap" rel="stylesheet">
<style>
  :root {
    --stage: #d9d9d9;
    --magenta-deep: #a8124f;
    --magenta: #c81e63;
    --magenta-light: #d6407c;
    --navy: #1e2f8a;
    --blue: #1b5fb0;
    --cyan: #12a4d1;
    --card-text: #f4f1ea;
    --mark: #2f3f9c;
  }
  * { margin: 0; padding: 0; box-sizing: border-box; }
  html, body { width: 1200px; height: 900px; overflow: hidden; }
  body {
    background: var(--stage);
    font-family: "Josefin Sans", sans-serif;
    color: var(--card-text);
    position: relative;
  }
  .card {
    position: absolute;
    width: 600px;
    height: 366px;
    border-radius: 3px;
    overflow: hidden;
    box-shadow: 0 10px 24px rgba(0,0,0,0.25);
  }
  /* Front */
  .card--front {
    left: 170px; top: 50px;
    background: linear-gradient(135deg, var(--magenta-deep), var(--magenta) 50%, var(--magenta-light));
  }
  .front__pattern {
    position: absolute; inset: 0;
    background: radial-gradient(ellipse at 25% 50%, rgba(255,90,170,0.25), transparent 60%),
                radial-gradient(ellipse at 80% 40%, rgba(255,90,170,0.22), transparent 55%);
  }
  .front__mark {
    position: absolute; left: 50%; top: 58px;
    width: 130px; height: 130px; margin-left: -65px;
    border-radius: 50%; background: var(--mark);
  }
  .front__name {
    position: absolute; left: 0; right: 0; top: 222px;
    text-align: center; font-size: 30px; font-weight: 400;
  }
  /* Back */
  .card--back {
    left: 430px; top: 484px;
    background: linear-gradient(200deg, var(--cyan) 0%, var(--blue) 45%, var(--navy) 100%);
  }
  .back__brand {
    position: absolute; left: 60px; top: 30px; width: 170px;
    display: flex; flex-direction: column; align-items: center; gap: 12px;
  }
  .back__mark { width: 120px; height: 120px; border-radius: 50%; background: var(--mark); }
  .back__brand-name { font-size: 17px; font-weight: 400; }
  .back__details { position: absolute; left: 270px; top: 52px; width: 300px; }
  .back__name { font-size: 24px; font-weight: 400; letter-spacing: 2px; text-transform: uppercase; }
  .back__creds { font-size: 12px; letter-spacing: 6px; text-transform: uppercase; margin-top: 2px; }
  .back__rule { border-top: 1px dotted var(--card-text); margin: 8px 0; opacity: 0.85; }
  .contact { list-style: none; font-size: 15px; font-weight: 300; }
  .contact li { display: flex; align-items: center; gap: 10px; line-height: 22px; }
  .contact svg { width: 16px; height: 14px; flex: none; }
  .back__address { font-size: 15px; font-weight: 300; }
  .back__roles {
    position: absolute; left: 24px; right: 18px; top: 300px;
    font-size: 13px; font-variant: small-caps; letter-spacing: 1.6px; font-weight: 400;
  }
</style>
</head>
<body>
  <section class="card card--front">
    <div class="front__pattern" role="img" aria-label="Decorative flowing vine and leaf pattern in soft pink tones"></div>
    <div class="front__mark"></div>
    <p class="front__name">Tessa Shiatsu</p>
  </section>

  <section class="card card--back">
    <div class="back__brand">
      <div class="back__mark"></div>
      <p class="back__brand-name">Tessa Shiatsu</p>
    </div>
    <div class="back__details">
      <h1 class="back__name">Tessa Gorrinde</h1>
      <p class="back__creds">BHSc. (Nat) m.QRPC</p>
      <div class="back__rule"></div>
      <ul class="contact">
        <li>
          <svg viewBox="0 0 16 14" aria-hidden="true"><path d="M4 1 L6 4 L5 6 Q7 9 9 10 L11 9 L14 11 L12 13 Q5 12 2 3 Z" fill="none" stroke="currentColor" stroke-width="1.2"/></svg>
          <span>: 0400 555 218</span>
        </li>
        <li>
          <svg viewBox="0 0 16 14" aria-hidden="true"><rect x="1" y="2" width="14" height="10" fill="none" stroke="currentColor" stroke-width="1.2"/><path d="M1 2 L8 8 L15 2" fill="none" stroke="currentColor" stroke-width="1.2"/></svg>
          <span>: tessa@tessagorrinde.com.au</span>
        </li>
        <li>
          <svg viewBox="0 0 16 14" aria-hidden="true"><circle cx="8" cy="7" r="6" fill="none" stroke="currentColor" stroke-width="1.2"/><ellipse cx="8" cy="7" rx="2.5" ry="6" fill="none" stroke="currentColor" stroke-width="1"/><path d="M2 7 H14" stroke="currentColor" stroke-width="1"/></svg>
          <span>: www.tessagorrinde.com.au</span>
        </li>
      </ul>
      <p class="back__address">41 Dovertan St South Karrowby</p>
      <div class="back__rule"></div>
    </div>
    <p class="back__roles">Naturopath, Herbalist, Nutritionist, Shiatsu Therapist, Wellness Counsellor</p>
  </section>
</body>
</html>
```